Brightmill Kitchens sell sheet

Make a 2 sided large format post card (5.5 x 8.5 inches) that introduces Brightmill Kitchens to prospective customers. Use the images and leave space for main selling points on front. Then leave space for a map and further details on the back.
PLEASE INCLUDE THE FOLLOWING CONTENT:
MAIN PAGE
heading:
Contract manufacturing & 3PL in Metro NYC
bullets:
Modern conveniently located facility with multiple lines. SQF, Kosher, Non-GMO, Organic, Gluten-Free.
Slabbing, single and coextrusion, baking, liquid & dry blending & filling.
3PL warehousing & fulfillment
BACK PAGE:
BrightMill Kitchens was created and is operated by experienced, successful natural food brand owners, as a higher-level contract manufacturing experience. Our goal is to provide the control and cost structure of self-manufacturing, while leveraging our capital investment and expertise.
You're always welcome to collaborate with us, observe your production and to enjoy our on-site fitness center, yoga classes, meditation, nursing and telework facilities.
Contact Owen Halvorsen 914-555-0163 owen@brightmill.example
Return address for postcard, should be small:
48 Larkspur Lane #517, Danbury CT 06811
Target Market(s)
B to B. We are an industrial contract manufacturer doing large volume production.
Industry/Entity Type
We design and manufacture natural food products for other companies to sell under their own brands.
Requirements
Must have
- Leave a small but adequate area for the postcard to be mailed. Must depict the some elements of all product stock images provided. Showing the full variety of food bars and product pouches and bottles we package so they are recognizable at a glance. The bar with the filling is not the major product, so even though it has it's own image, the other bars should be more prominent.
Nice to have
- A map same or similar to the one shown. The circle depicts the necessary visible radius. It can also be rectangular.

```html
<!DOCTYPE html>
<html lang="en">
<head>
<meta charset="utf-8">
<title>Brightmill Kitchens Postcard</title>
<link rel="stylesheet" href="https://fonts.googleapis.com/css2?family=Oswald:wght@500&family=Open+Sans:wght@400;600&display=swap">
<style>
  :root {
    --canvas: #e4e4e2;
    --paper: #ffffff;
    --paper-warm: #f1f0ee;
    --red: #e8394f;
    --pink: #e01a5e;
    --green: #a8c94a;
    --ink: #4a4a4a;
    --rule: #b9b9b9;
    --line: #c7c7c7;
  }
  * { box-sizing: border-box; margin: 0; padding: 0; }
  html, body { width: 1200px; height: 1102px; overflow: hidden; }
  body {
    background: var(--canvas);
    font-family: "Open Sans", Arial, sans-serif;
    color: var(--ink);
    position: relative;
  }
  .card {
    position: absolute;
    width: 760px;
    height: 492px;
    background: var(--paper);
    box-shadow: 0 6px 18px rgba(0,0,0,.18);
    overflow: hidden;
  }
  .card--front { left: 50px; top: 40px; background: var(--paper-warm); }
  .card--back { left: 390px; top: 580px; }
  .card-art { position: absolute; inset: 0; }

  .brand {
    position: absolute;
    display: flex;
    align-items: center;
    gap: 8px;
    font-family: "Oswald", sans-serif;
    font-weight: 500;
    color: var(--red);
    text-transform: uppercase;
    line-height: 1.05;
  }
  .brand-dot { width: 30px; height: 30px; border-radius: 50%; background: var(--red); flex: none; }
  .card--front .brand { left: 34px; top: 96px; font-size: 22px; }
  .card--back .brand { left: 232px; top: 140px; font-size: 18px; background: var(--paper); padding: 6px 10px 6px 6px; border-radius: 24px; }

  .front-heading {
    position: absolute; left: 40px; top: 174px; width: 330px;
    font-family: "Oswald", sans-serif; font-weight: 500;
    color: var(--red); font-size: 19px; line-height: 1.2; text-transform: uppercase;
  }

  .selling-points { position: absolute; left: 40px; top: 246px; width: 340px; list-style: none; }
  .selling-points li {
    display: flex; align-items: center; gap: 9px;
    font-size: 11.5px; height: 26px; white-space: nowrap;
    border-bottom: 1px dotted var(--rule);
  }
  .point-icon { width: 16px; height: 16px; border-radius: 50%; border: 1.5px solid var(--red); flex: none; position: relative; }
  .point-icon::after { content: ""; position: absolute; left: 4px; top: 4px; width: 5px; height: 5px; border-radius: 50%; background: var(--red); }

  .contact-row { position: absolute; display: flex; align-items: center; font-size: 12.5px; white-space: nowrap; }
  .contact-item { display: flex; align-items: center; gap: 7px; }
  .contact-icon { width: 15px; height: 15px; flex: none; }
  .card--front .contact-row { left: 230px; top: 438px; gap: 30px; color: var(--ink); }
  .card--back .contact-row { left: 22px; top: 458px; gap: 22px; color: var(--paper); font-size: 11.5px; }

  .find-tag {
    position: absolute;
    background: var(--green);
    color: var(--paper);
    font-family: "Oswald", sans-serif;
    font-weight: 500;
    font-size: 17px;
    text-transform: uppercase;
    padding: 2px 26px 2px 18px;
    border-radius: 0 20px 20px 0;
    white-space: nowrap;
  }
  .card--front .find-tag { left: 0; top: 454px; }
  .card--back .find-tag { left: 0; top: 416px; }

  .back-heading {
    position: absolute; left: 34px; top: 134px; width: 190px;
    font-family: "Oswald", sans-serif; font-weight: 500;
    color: var(--red); font-size: 17px; line-height: 1.2; text-transform: uppercase;
  }
  .back-copy { position: absolute; left: 34px; top: 186px; width: 280px; font-size: 9.6px; line-height: 1.38; }
  .back-copy p + p { margin-top: 5px; }

  .return-address { position: absolute; left: 372px; top: 62px; width: 200px; font-size: 9px; line-height: 1.35; color: var(--ink); }
  .address-lines { position: absolute; left: 420px; top: 198px; width: 280px; }
  .address-lines span { display: block; height: 38px; border-bottom: 1.5px solid var(--line); }
  .stamp-box { position: absolute; left: 610px; top: 36px; width: 92px; height: 80px; border: 1.5px solid var(--line); }
</style>
</head>
<body>

<section class="card card--front" aria-label="Postcard front">
  <svg class="card-art" width="760" height="492" viewBox="0 0 760 492">
    <defs>
      <linearGradient id="fillingBar" x1="0" y1="0" x2="1" y2="1">
        <stop offset="0" stop-color="#e0b987"/><stop offset=".55" stop-color="#b84a4a"/><stop offset="1" stop-color="#cfa170"/>
      </linearGradient>
      <linearGradient id="barsRow" x1="0" y1="0" x2="1" y2="0">
        <stop offset="0" stop-color="#d9a96a"/><stop offset=".4" stop-color="#8c5a45"/><stop offset=".7" stop-color="#e9dcc3"/><stop offset="1" stop-color="#b86b5c"/>
      </linearGradient>
    </defs>
    <circle class="front-panel" cx="660" cy="140" r="270" fill="var(--paper)" stroke="var(--red)" stroke-width="5"/>
    <ellipse role="img" aria-label="Photo of a fruit-filled bar broken in half" cx="590" cy="118" rx="130" ry="82" fill="url(#fillingBar)" opacity=".85"/>
    <circle role="img" aria-label="Photo of a white spouted product pouch" cx="500" cy="300" r="56" fill="#eaeaea" stroke="var(--pink)" stroke-width="4"/>
    <circle role="img" aria-label="Photo of an assortment of food bars" cx="660" cy="290" r="86" fill="url(#barsRow)" stroke="var(--red)" stroke-width="5"/>
    <path class="swoosh" d="M0 398 C200 436 460 430 760 340 L760 372 C470 450 220 456 0 424 Z" fill="var(--pink)"/>
    <path class="footer-band" d="M0 424 C220 456 470 450 760 372 L760 492 L0 492 Z" fill="var(--paper)"/>
  </svg>

  <div class="brand"><span class="brand-dot"></span>Brightmill<br>Kitchens</div>

  <h1 class="front-heading">Contract manufacturing &amp; 3PL in Metro NYC</h1>

  <ul class="selling-points">
    <li><span class="point-icon"></span>Modern conveniently located facility with multiple lines</li>
    <li><span class="point-icon"></span>SQF, Kosher, Non-GMO, Organic, Gluten-Free</li>
    <li><span class="point-icon"></span>Slabbing, single and coextrusion, baking</li>
    <li><span class="point-icon"></span>Liquid &amp; dry blending &amp; filling</li>
    <li><span class="point-icon"></span>3PL warehousing &amp; fulfillment</li>
  </ul>

  <div class="contact-row">
    <span class="contact-item">
      <svg class="contact-icon" viewBox="0 0 16 16"><circle cx="8" cy="8" r="8" fill="var(--red)"/><rect x="4" y="5" width="8" height="6" fill="none" stroke="#fff" stroke-width="1.2"/><path d="M4 5 L8 8.5 L12 5" fill="none" stroke="#fff" stroke-width="1.2"/></svg>
      owen@brightmill.example
    </span>
    <span class="contact-item">
      <svg class="contact-icon" viewBox="0 0 16 16"><circle cx="8" cy="8" r="7.2" fill="none" stroke="var(--red)" stroke-width="1.4"/><path d="M5.5 4.5 L7 6.5 L6 7.5 C6.6 8.8 7.3 9.5 8.5 10 L9.5 9 L11.5 10.5 L10.5 12 C7.5 11.5 4.5 8.5 4 5.5 Z" fill="var(--red)"/></svg>
      914-555-0163
    </span>
    <span class="contact-item">
      <svg class="contact-icon" viewBox="0 0 16 16"><circle cx="8" cy="8" r="7.2" fill="none" stroke="var(--red)" stroke-width="1.4"/><ellipse cx="8" cy="8" rx="3" ry="5.5" fill="none" stroke="var(--red)" stroke-width="1"/><path d="M2.5 8 H13.5" stroke="var(--red)" stroke-width="1"/></svg>
      www.brightmill.example
    </span>
  </div>

  <div class="find-tag">Find more about us</div>
</section>

<section class="card card--back" aria-label="Postcard back">
  <svg class="card-art" width="760" height="492" viewBox="0 0 760 492">
    <defs>
      <linearGradient id="barsStrip" x1="0" y1="0" x2="1" y2="0">
        <stop offset="0" stop-color="#c88d55"/><stop offset=".3" stop-color="#9aa05a"/><stop offset=".55" stop-color="#5a3a32"/><stop offset=".8" stop-color="#e8d9bd"/><stop offset="1" stop-color="#c7744f"/>
      </linearGradient>
    </defs>
    <path class="back-panel" d="M0 0 L300 0 C250 120 340 160 330 250 C320 330 290 390 330 492 L0 492 Z" fill="var(--paper-warm)"/>
    <path class="back-curve" d="M300 0 C250 120 340 160 330 250 C320 330 290 390 330 492" fill="none" stroke="var(--red)" stroke-width="10"/>
    <rect role="img" aria-label="Photo of a row of assorted food bars" x="0" y="0" width="300" height="120" fill="url(#barsStrip)" opacity=".9"/>
    <path class="band-curve" d="M240 120 C290 104 320 40 420 20 C460 12 420 0 400 0 L300 0 C280 60 270 100 240 120 Z" fill="var(--red)" opacity=".9"/>
    <rect role="img" aria-label="Street map of the facility location and delivery radius" x="34" y="338" width="258" height="70" fill="#dfe8dc"/>
    <path class="footer-band" d="M0 444 L326 444 C328 462 329 478 332 492 L0 492 Z" fill="var(--red)"/>
  </svg>

  <div class="brand"><span class="brand-dot"></span>Brightmill<br>Kitchens</div>

  <h2 class="back-heading">Contract manufacturing &amp; 3PL</h2>
  <div class="back-copy">
    <p>BrightMill Kitchens was created and is operated by experienced, successful natural food brand owners, as a higher-level contract manufacturing experience. Our goal is to provide the control and cost structure of self-manufacturing, while leveraging our capital investment and expertise.</p>
    <p>You're always welcome to collaborate with us, observe your production and to enjoy our on-site fitness center, yoga classes, meditation, nursing and telework facilities.</p>
  </div>

  <div class="find-tag">Contact Owen Halvorsen</div>

  <div class="contact-row">
    <span class="contact-item">
      <svg class="contact-icon" viewBox="0 0 16 16"><circle cx="8" cy="8" r="7.2" fill="none" stroke="#fff" stroke-width="1.4"/><path d="M5.5 4.5 L7 6.5 L6 7.5 C6.6 8.8 7.3 9.5 8.5 10 L9.5 9 L11.5 10.5 L10.5 12 C7.5 11.5 4.5 8.5 4 5.5 Z" fill="#fff"/></svg>
      914-555-0163
    </span>
    <span class="contact-item">
      <svg class="contact-icon" viewBox="0 0 16 16"><circle cx="8" cy="8" r="7.2" fill="none" stroke="#fff" stroke-width="1.4"/><rect x="4" y="5" width="8" height="6" fill="none" stroke="#fff" stroke-width="1.2"/><path d="M4 5 L8 8.5 L12 5" fill="none" stroke="#fff" stroke-width="1.2"/></svg>
      owen@brightmill.example
    </span>
  </div>

  <address class="return-address">Brightmill Kitchens<br>48 Larkspur Lane #517, Danbury CT 06811</address>
  <div class="stamp-box"></div>
  <div class="address-lines"><span></span><span></span><span></span></div>
</section>

</body>
</html>
```